The Hollender House Brochure - A Real Estate Sales Brochure

I am a areal estate agent. This Brochure is for the marketing and sale of a historic home in an urban core, nationally recognized historic district. The community this home is located in, is Historic Maplecrest in Jacksonville Florida. This community borders the city core and provides quick and easy access to the heart of Jacksonville and the downtown scene.

The type of people who live in Historic Maplecrest are diverse. Virtually every race, religion and socio economic class are represented in this community. We want to develop a brochure that appeals to an urban hipster, younger buyer.
Updates

Target Market(s)

Younger home buyers who want to live close to the urban core of a metropolitan area. Ages 25 - 45 with annual income of $75,000 +

Industry/Entity Type

Real Estate

Font styles to use
Sans Serif

Requirements
Must have
• Four page brochure.
Nice to have
• Sample copy provided below:
• WOW!! The 3,288 sf Grand Dame of the Maplecrest Historic District. This Vintage home has been completely renovated. Updated wiring, plumbing, blown in insulation, Vorlex tankless gas hot water heaters, newer windows and HVAC. Also features new exterior paint, interior paint, lighting, crisp new kitchen with stainless appliances. This spacious property provides lots of living options. Four bedrooms, four baths, two kitchens, four living areas and four gas fireplaces. Main home is approx. 2,400 sf with an additional one bedroom, one bath 900 sf apartment. Keep the apartment for visiting guests or rent it and defray your monthly housing cost. On the best Street in Historic Maplecrest, this home is literally steps away from beautiful Brenner Park and downtown Jacksonville. Convenience, comfort and style. This is home!

```html
<!DOCTYPE html>
<html lang="en">
<head>
<meta charset="utf-8">
<title>The Hollender House Brochure</title>
<link rel="stylesheet" href="https://fonts.googleapis.com/css2?family=Arimo:wght@400;700&family=Lato:wght@400;700&display=swap">
<style>
  :root {
    --backdrop: #e4e4e4;
    --paper: #ffffff;
    --paper-grey: #eceef0;
    --ink: #2f2f2f;
    --ink-soft: #5b5b5b;
    --orange: #e2681f;
    --orange-deep: #cf5612;
    --orange-light: #ee8a3c;
    --band: #1b1b1b;
    --gold: #c9a45a;
    --silver-top: #f7f7f7;
    --silver-bottom: #d3d5d8;
  }
  * { box-sizing: border-box; margin: 0; padding: 0; }
  html, body { width: 1200px; height: 876px; overflow: hidden; }
  body {
    background: radial-gradient(ellipse at 50% 40%, #f2f2f2 0%, var(--backdrop) 75%);
    font-family: "Arimo", Arial, sans-serif;
    position: relative;
  }
  .spread {
    position: absolute; left: 70px; top: 68px;
    width: 1060px; height: 740px;
    display: flex;
    box-shadow: 0 14px 40px rgba(0,0,0,.22);
  }
  .page { position: relative; width: 530px; height: 740px; overflow: hidden; background: var(--paper); }

  /* ---- inside page ---- */
  .page--inside { background: linear-gradient(180deg, #ffffff 0%, var(--paper-grey) 100%); }
  .kitchen-photo {
    position: absolute; left: 0; top: 0; width: 530px; height: 470px;
    background: linear-gradient(160deg, #f1ede6 0%, #dcd4c8 35%, #b7a48d 60%, #8a5a36 85%, #6f4428 100%);
  }
  .about-panel {
    position: absolute; left: 22px; top: 50px; width: 270px; height: 340px;
    background: rgba(255,255,255,.72);
    padding: 12px 14px;
    font-family: "Lato", sans-serif; color: var(--ink);
  }
  .about-panel h2 { font-size: 15px; font-weight: 700; margin-bottom: 4px; line-height: 1.2; }
  .about-panel p { font-size: 9px; line-height: 1.32; text-align: justify; margin-bottom: 6px; }
  .about-panel p:last-child { margin-bottom: 0; }
  .band { position: absolute; left: 0; width: 530px; }
  .band--inside { top: 420px; height: 70px; }
  .thumb {
    position: absolute; top: 404px; width: 168px; height: 122px;
    border-radius: 14px; border: 3px solid var(--gold);
    box-shadow: 0 3px 8px rgba(0,0,0,.25);
  }
  .thumb--park { left: 70px; background: linear-gradient(170deg, #7d8a6a 0%, #c9d3c4 45%, #e8ece6 70%, #6e8a5a 100%); }
  .thumb--bath { left: 252px; background: linear-gradient(180deg, #2f5fd0 0%, #5f88d8 22%, #f3f5f7 40%, #dfe3e8 100%); }
  .community-box {
    position: absolute; left: 55px; top: 565px; width: 440px; height: 112px;
    border: 2px solid var(--gold); border-radius: 16px;
    background: linear-gradient(180deg, #ffffff 0%, #f1f2f3 100%);
    box-shadow: 0 4px 10px rgba(0,0,0,.12);
    display: flex; flex-direction: column; justify-content: center; align-items: center;
    text-align: center; color: var(--ink-soft); font-size: 13px; line-height: 1.35; padding: 0 18px;
  }
  .community-box p + p { margin-top: 8px; }

  /* ---- cover page ---- */
  .cover-header {
    position: absolute; left: 0; top: 0; width: 530px; height: 66px;
    background: linear-gradient(180deg, var(--silver-top) 0%, var(--silver-bottom) 100%);
    text-align: center; padding-top: 10px;
  }
  .cover-header .kicker { font-size: 20px; color: #4a4a4a; letter-spacing: .5px; line-height: 1.05; }
  .cover-header .city { font-size: 20px; font-weight: 700; color: var(--orange); letter-spacing: .5px; line-height: 1.1; }
  .parlor-photo {
    position: absolute; left: 0; top: 66px; width: 530px; height: 410px;
    background: linear-gradient(180deg, #c9b96a 0%, #d9cd84 42%, #cfc7a0 58%, #6c6c6c 74%, #e8e8e8 100%);
  }
  .band--cover { top: 392px; height: 90px; }
  .cover-panel {
    position: absolute; left: 0; top: 470px; width: 530px; height: 270px;
    background: linear-gradient(160deg, var(--orange-light) 0%, var(--orange) 45%, var(--orange-deep) 100%);
    color: #fff; text-align: center; padding-top: 50px;
  }
  .cover-panel .rule { width: 300px; height: 1px; margin: 0 auto; background: linear-gradient(90deg, transparent, #fff, transparent); }
  .cover-panel h1 { font-size: 30px; font-weight: 400; margin-top: 10px; line-height: 1; }
  .cover-panel .tag { font-size: 20px; line-height: 1.1; }
  .cover-panel .sub { font-size: 14px; margin-bottom: 10px; }
</style>
</head>
<body>
  <div class="spread">
    <section class="page page--inside">
      <div class="kitchen-photo" role="img" aria-label="Renovated kitchen with white cabinets, stainless appliances and wood floor"></div>
      <div class="about-panel">
        <h2>About Us</h2>
        <p>Lorem Ipsum is simply dummy text of the printing and typesetting industry. Lorem Ipsum has been the industry's standard dummy text ever since the 1500s, when an unknown printer took a galley of type and scrambled it to make a type specimen book. It has survived not only five centuries, but also the leap into electronic typesetting.</p>
        <p>Remaining essentially unchanged. It was popularised in the 1960s with the release of Typeframe sheets containing Lorem Ipsum passages, and more recently with desktop publishing software like Quillset Layout including versions of Lorem Ipsum. It is a long established fact that a reader will be distracted by the readable content of a page when looking at its layout. The point of using Lorem Ipsum is that it has a more-or-less normal distribution of letters, as opposed to using 'Content here, content here', making it look like readable English. Many desktop publishing packages and web page editors now use Lorem Ipsum as their default model text. Various versions have evolved over the years, sometimes by accident, sometimes on purpose (injected humour and the like).</p>
      </div>
      <svg class="band band--inside" viewBox="0 0 530 70" preserveAspectRatio="none" aria-hidden="true">
        <polygon points="0,30 530,0 530,28 0,58" fill="var(--band)"/>
      </svg>
      <div class="thumb thumb--park" role="img" aria-label="Park pavilion under oak trees"></div>
      <div class="thumb thumb--bath" role="img" aria-label="Bathroom with blue ceiling and white fixtures"></div>
      <div class="community-box">
        <p>The community this home is located in, is Historic Maplecrest<br>in Jacksonville Florida.</p>
        <p>This community borders the city core and provides quick and easy<br>access to the heart of Jacksonville and the downtown scene.</p>
      </div>
    </section>

    <section class="page page--cover">
      <header class="cover-header">
        <div class="kicker">HISTORIC MAPLECREST IN</div>
        <div class="city">JACKSONVILLE FLORIDA</div>
      </header>
      <div class="parlor-photo" role="img" aria-label="Parlor with yellow walls, tiled fireplace and checkerboard floor"></div>
      <svg class="band band--cover" viewBox="0 0 530 90" preserveAspectRatio="none" aria-hidden="true">
        <polygon points="0,78 530,20 530,60 0,90" fill="var(--band)"/>
      </svg>
      <div class="cover-panel">
        <div class="rule"></div>
        <h1>WOW!!</h1>
        <div class="tag">THE 3,288 SF GRAND DAME</div>
        <div class="sub">OF THE MAPLECREST HISTORIC DISTRICT.</div>
        <div class="rule"></div>
      </div>
    </section>
  </div>
</body>
</html>
```